Need A Standard Musical Download Website

We are looking for a talented designer to create a unique web design for our startup Music website called Vorlen Music.
The website should be responsive and filled with some creative stuffs along with bright colors.

Vorlen music is a website loaded with different types of music and capable of downloading the requested music by its users.
There will be categories of music which would be sorted by the genre. They include RnB, Hip-Hop, Afro pop, Pop, Dancehall and Reggae).

DESIGN STYLE/THEME

Creative, trendy, colorful, unique, and easy to use. You have freedom of selecting which ever color suits you. The design must be energetic and attractive.

NAVIGATION

HOME-MUSIC(RnB, Hip hop, Afro pop, POP, dancehall, Reggae)-ARTISTE-NEWS-LOGIN

PAGES REQUIRED
------------
1)Home Page
2)Music

FONTS
GOOGLE FONTS is strongly recommended.

Designers can get inspiration from https://tunebarrowk.com

Industry/Entity Type

Startup

```html
<!DOCTYPE html>
<html lang="en">
<head>
<meta charset="utf-8">
<title>Vorlen Music — Music</title>
<link href="https://fonts.googleapis.com/css2?family=Montserrat:wght@400;500;600;700&display=swap" rel="stylesheet">
<style>
:root{
  --black:#050505;
  --teal:#0f6e93;
  --orange:#f39a1f;
  --red:#e5403a;
  --blue:#2aa7d6;
  --ink:#333;
  --muted:#9a9a9a;
  --tabbar:#e4e4e4;
  --line:#dedede;
  --white:#fff;
}
*{margin:0;padding:0;box-sizing:border-box}
html,body{width:1142px;height:1200px;overflow:hidden;background:var(--white);font-family:'Montserrat',sans-serif}
.page{position:relative;width:1142px;height:1200px;overflow:hidden}
.abs{position:absolute}

/* header */
.site-header{left:0;top:0;width:1142px;height:62px;background:var(--black)}
.brand{left:137px;top:18px;color:var(--white);font-size:22px;font-weight:600;letter-spacing:-.5px}
.main-nav{left:520px;top:25px;display:flex;gap:18px;font-size:10px;font-weight:600;color:#ddd}
.main-nav .active{color:var(--orange)}
.search{left:758px;top:18px;width:173px;height:24px;border:1px solid #555;border-radius:12px;color:#777;font-size:9px;padding:6px 11px;letter-spacing:.5px}
.search .btn{position:absolute;right:-1px;top:-1px;width:25px;height:24px;background:#555;border-radius:0 12px 12px 0}
.login{left:939px;top:18px;width:66px;height:24px;border-radius:12px;background:var(--teal);color:var(--white);font-size:10px;font-weight:600;text-align:center;line-height:24px}

/* hero player */
.hero{left:0;top:62px;width:1142px;height:188px;background:linear-gradient(90deg,#2b1060,#1c1a6e 45%,#1a2a8a 100%)}
.cover{left:160px;top:107px;width:169px;height:95px;background:linear-gradient(120deg,#d9b48a,#b46a45 55%,#3b2218)}
.now{top:111px;font-size:11.5px;font-weight:500;color:var(--white)}
.now b{color:var(--orange);font-weight:500}
.ctrl{top:141px}
.time{top:145px;color:var(--white);font-size:9px}
.track{left:470px;top:149px;width:278px;height:4px;background:#241f55;border-radius:2px}
.track i{position:absolute;left:0;top:-3px;width:10px;height:10px;border-radius:50%;background:var(--white)}
.vol{left:910px;top:149px;width:71px;height:3px;background:#35326b}
.vol i{position:absolute;left:0;top:0;width:34px;height:3px;background:#8f8ac7}
.act{top:176px;display:flex;align-items:center;gap:6px;font-size:7px;font-weight:600;line-height:1}
.act .dot{width:26px;height:26px;border-radius:50%;display:flex;align-items:center;justify-content:center}

/* colour bands */
.band{left:0;width:1142px}

/* music panel */
.panel{left:137px;top:318px;width:868px;height:583px;border:1px solid var(--line);background:var(--white)}
.tabbar{left:0;top:0;width:866px;height:36px;background:var(--tabbar)}
.tab{top:0;height:36px;line-height:36px;font-size:11px;font-weight:500;color:var(--white)}
.genres{left:186px;top:0;height:36px;display:flex;align-items:center;gap:23px;font-size:11px;font-weight:500;color:var(--muted)}
.genres .on,.artist-lbl{color:var(--teal);font-weight:600}
.artist-lbl{left:611px;top:12px;font-size:11px}
.select{left:656px;top:7px;width:173px;height:22px;border:1px solid #ccc;border-radius:11px;background:var(--white);font-size:9px;color:#888;padding:5px 11px}
.select .arr{position:absolute;right:-1px;top:-1px;width:25px;height:22px;background:#ccc;border-radius:0 11px 11px 0}
.divider{left:434px;top:67px;width:1px;height:442px;background:#f1c89a}
.col{top:64px;width:400px}
.row{position:relative;height:57px}
.thumb{position:absolute;left:0;top:6px;width:34px;height:34px;background:linear-gradient(130deg,#d6a57e,#a4513a 60%,#2d1a14)}
.play{position:absolute;left:42px;top:7px;width:30px;height:30px;border:1.5px solid #bbb;border-radius:50%}
.play:after{content:"";position:absolute;left:11px;top:7px;border-left:10px solid #aaa;border-top:7px solid transparent;border-bottom:7px solid transparent}
.title{position:absolute;left:78px;top:13px;font-size:9.5px;font-weight:500;color:var(--ink)}
.artist{position:absolute;left:78px;top:27px;font-size:8px;font-weight:600;color:var(--orange)}
.ic{position:absolute;top:7px;width:30px;height:30px;border-radius:50%;border:1.5px solid;display:flex;align-items:center;justify-content:center}
.ic.h{left:270px;border-color:var(--red)}
.ic.d{left:305px;border-color:var(--blue)}
.ic.s{left:340px;border-color:var(--orange)}
.more{left:754px;top:537px;font-size:9.5px;font-weight:600;color:var(--orange)}

/* footer */
.footer{left:0;top:970px;width:1142px;height:184px;background:linear-gradient(90deg,#5a1680,#3a1f8c 50%,#1b3597)}
.f-brand{left:137px;top:1024px;color:var(--white);font-size:22px;font-weight:600;letter-spacing:-.5px}
.social{left:186px;top:1062px;display:flex;gap:5px}
.social span{width:18px;height:18px;border-radius:50%}
.f-links{top:1030px;display:flex;flex-direction:column;gap:6px;font-size:10px;font-weight:600;color:#e8e6f2;line-height:13px}
.news-h{left:805px;top:1030px;font-size:10px;font-weight:600;color:#e8e6f2}
.email{left:805px;top:1049px;width:200px;height:30px;background:var(--white);font-size:9.5px;color:#333;padding:9px 8px}
.submit{left:805px;top:1087px;width:70px;height:26px;background:var(--teal);color:#cfe7f2;font-size:11px;font-weight:600;text-align:center;line-height:26px}
.legal{left:0;top:1154px;width:1142px;height:46px;background:var(--black);color:#888;font-size:9.5px;font-weight:600;text-align:center;line-height:50px}
</style>
</head>
<body>
<svg width="0" height="0" style="position:absolute">
  <defs>
    <symbol id="i-heart" viewBox="0 0 24 24"><path d="M12 21s-8-5.2-8-11a4.5 4.5 0 0 1 8-2.8A4.5 4.5 0 0 1 20 10c0 5.8-8 11-8 11z"/></symbol>
    <symbol id="i-down" viewBox="0 0 24 24"><path d="M12 3v11M7 9l5 5 5-5M4 15v5h16v-5" fill="none" stroke-width="2.2"/></symbol>
    <symbol id="i-share" viewBox="0 0 24 24"><path d="M17 4L7 12l10 8" fill="none" stroke-width="2"/><circle cx="17" cy="4" r="2"/><circle cx="7" cy="12" r="2"/><circle cx="17" cy="20" r="2"/></symbol>
  </defs>
</svg>
<div class="page">
  <header class="abs site-header"></header>
  <div class="abs brand">Vorlen Music</div>
  <nav class="abs main-nav"><span>HOME</span><span class="active">MUSIC</span><span>ARTISTS</span><span>NEWS</span></nav>
  <div class="abs search">SEARCH<span class="btn"></span></div>
  <div class="abs login">LOGIN</div>

  <section class="abs hero"></section>
  <div class="abs cover" role="img" aria-label="Album cover: Rock &amp; Roll 2017 - Reloaded, singer with sunglasses"></div>
  <div class="abs now" style="left:443px"><b>PLAYING NOW :</b> ROCK &amp; ROLL 2017 - RELOADED</div>
  <div class="abs now" style="left:751px"><b>ARTIST :</b> MARLO KEATS</div>
  <svg class="abs ctrl" style="left:352px" width="66" height="20" viewBox="0 0 66 20" fill="#fff">
    <rect x="2" y="5" width="2" height="10"/><path d="M12 5v10L4 10z"/>
    <path d="M30 1v18l14-9z"/>
    <path d="M55 5v10l8-5z"/><rect x="63" y="5" width="2" height="10"/>
  </svg>
  <div class="abs time" style="left:437px">0:00</div>
  <div class="abs track"><i></i></div>
  <div class="abs time" style="left:756px">0:00</div>
  <svg class="abs ctrl" style="left:804px" width="100" height="20" viewBox="0 0 100 20" fill="none" stroke="#fff" stroke-width="2">
    <path d="M1 5h4l8 10h4M1 15h4l8-10h4M14 2l3 3-3 3M14 12l3 3-3 3"/>
    <path d="M39 10V6h16M39 14h16v-4M52 3l3 3-3 3"/>
    <path d="M80 7h4l5-4v14l-5-4h-4z" fill="#fff"/><path d="M92 6q3 4 0 8M95 4q5 6 0 12"/>
  </svg>
  <div class="abs vol"><i></i></div>
  <div class="abs act" style="left:574px;color:var(--red)"><span class="dot" style="background:var(--red)"><svg width="13" height="13" fill="#fff"><use href="#i-heart"/></svg></span>ADD TO<br>PLAYLIST</div>
  <div class="abs act" style="left:670px;color:var(--blue)"><span class="dot" style="background:var(--teal)"><svg width="13" height="13" stroke="#fff"><use href="#i-down"/></svg></span>DOWNLOAD<br>NOW</div>

  <svg class="abs band" style="top:248px" width="1142" height="48" viewBox="0 0 1142 48">
    <defs><linearGradient id="g1" x1="0" x2="1"><stop offset="0" stop-color="#d8283a"/><stop offset=".45" stop-color="#ee5a25"/><stop offset=".75" stop-color="#f39a1f"/><stop offset="1" stop-color="#f6c22a"/></linearGradient></defs>
    <polygon points="0,0 1142,0 1142,2 1008,46 0,4" fill="url(#g1)"/>
  </svg>

  <section class="abs panel">
    <div class="abs tabbar"></div>
    <svg class="abs" style="left:0;top:0" width="166" height="36"><polygon points="0,0 82,0 54,36 0,36" fill="#e8453f"/><polygon points="82,0 166,0 140,36 54,36" fill="#cfcfcf"/></svg>
    <div class="abs tab" style="left:20px">MP3</div>
    <div class="abs tab" style="left:89px">VIDEO</div>
    <nav class="abs genres"><span class="on">RNB</span><span>HIP-HOP</span><span>AFRO POP</span><span>POP</span><span>DANCEHALL</span><span>REGGAE</span></nav>
    <div class="abs artist-lbl">ARTIST</div>
    <div class="abs select">ALL<span class="arr"></span></div>
    <div class="abs divider"></div>

    <div class="abs col" style="left:37px">
      <div class="row"><span class="thumb" role="img" aria-label="Track cover"></span><span class="play"></span><span class="title">ROCK &amp; ROLL 2017 - RELOADED</span><span class="artist">MARLO KEATS</span><span class="ic h"><svg width="13" height="13" fill="var(--red)"><use href="#i-heart"/></svg></span><span class="ic d"><svg width="13" height="13" stroke="var(--blue)"><use href="#i-down"/></svg></span><span class="ic s"><svg width="13" height="13" stroke="var(--orange)" fill="var(--orange)"><use href="#i-share"/></svg></span></div>
      <div class="row"><span class="thumb" role="img" aria-label="Track cover"></span><span class="play"></span><span class="title">ROCK &amp; ROLL 2017 - RELOADED</span><span class="artist">MARLO KEATS</span><span class="ic h"><svg width="13" height="13" fill="var(--red)"><use href="#i-heart"/></svg></span><span class="ic d"><svg width="13" height="13" stroke="var(--blue)"><use href="#i-down"/></svg></span><span class="ic s"><svg width="13" height="13" stroke="var(--orange)" fill="var(--orange)"><use href="#i-share"/></svg></span></div>
      <div class="row"><span class="thumb" role="img" aria-label="Track cover"></span><span class="play"></span><span class="title">ROCK &amp; ROLL 2017 - RELOADED</span><span class="artist">MARLO KEATS</span><span class="ic h"><svg width="13" height="13" fill="var(--red)"><use href="#i-heart"/></svg></span><span class="ic d"><svg width="13" height="13" stroke="var(--blue)"><use href="#i-down"/></svg></span><span class="ic s"><svg width="13" height="13" stroke="var(--orange)" fill="var(--orange)"><use href="#i-share"/></svg></span></div>
      <div class="row"><span class="thumb" role="img" aria-label="Track cover"></span><span class="play"></span><span class="title">ROCK &amp; ROLL 2017 - RELOADED</span><span class="artist">MARLO KEATS</span><span class="ic h"><svg width="13" height="13" fill="var(--red)"><use href="#i-heart"/></svg></span><span class="ic d"><svg width="13" height="13" stroke="var(--blue)"><use href="#i-down"/></svg></span><span class="ic s"><svg width="13" height="13" stroke="var(--orange)" fill="var(--orange)"><use href="#i-share"/></svg></span></div>
      <div class="row"><span class="thumb" role="img" aria-label="Track cover"></span><span class="play"></span><span class="title">ROCK &amp; ROLL 2017 - RELOADED</span><span class="artist">MARLO KEATS</span><span class="ic h"><svg width="13" height="13" fill="var(--red)"><use href="#i-heart"/></svg></span><span class="ic d"><svg width="13" height="13" stroke="var(--blue)"><use href="#i-down"/></svg></span><span class="ic s"><svg width="13" height="13" stroke="var(--orange)" fill="var(--orange)"><use href="#i-share"/></svg></span></div>
      <div class="row"><span class="thumb" role="img" aria-label="Track cover"></span><span class="play"></span><span class="title">ROCK &amp; ROLL 2017 - RELOADED</span><span class="artist">MARLO KEATS</span><span class="ic h"><svg width="13" height="13" fill="var(--red)"><use href="#i-heart"/></svg></span><span class="ic d"><svg width="13" height="13" stroke="var(--blue)"><use href="#i-down"/></svg></span><span class="ic s"><svg width="13" height="13" stroke="var(--orange)" fill="var(--orange)"><use href="#i-share"/></svg></span></div>
      <div class="row"><span class="thumb" role="img" aria-label="Track cover"></span><span class="play"></span><span class="title">ROCK &amp; ROLL 2017 - RELOADED</span><span class="artist">MARLO KEATS</span><span class="ic h"><svg width="13" height="13" fill="var(--red)"><use href="#i-heart"/></svg></span><span class="ic d"><svg width="13" height="13" stroke="var(--blue)"><use href="#i-down"/></svg></span><span class="ic s"><svg width="13" height="13" stroke="var(--orange)" fill="var(--orange)"><use href="#i-share"/></svg></span></div>
      <div class="row"><span class="thumb" role="img" aria-label="Track cover"></span><span class="play"></span><span class="title">ROCK &amp; ROLL 2017 - RELOADED</span><span class="artist">MARLO KEATS</span><span class="ic h"><svg width="13" height="13" fill="var(--red)"><use href="#i-heart"/></svg></span><span class="ic d"><svg width="13" height="13" stroke="var(--blue)"><use href="#i-down"/></svg></span><span class="ic s"><svg width="13" height="13" stroke="var(--orange)" fill="var(--orange)"><use href="#i-share"/></svg></span></div>
    </div>

    <div class="abs col" style="left:467px">
      <div class="row"><span class="thumb" role="img" aria-label="Track cover"></span><span class="play"></span><span class="title">ROCK &amp; ROLL 2017 - RELOADED</span><span class="artist">MARLO KEATS</span><span class="ic h"><svg width="13" height="13" fill="var(--red)"><use href="#i-heart"/></svg></span><span class="ic d"><svg width="13" height="13" stroke="var(--blue)"><use href="#i-down"/></svg></span><span class="ic s"><svg width="13" height="13" stroke="var(--orange)" fill="var(--orange)"><use href="#i-share"/></svg></span></div>
      <div class="row"><span class="thumb" role="img" aria-label="Track cover"></span><span class="play"></span><span class="title">ROCK &amp; ROLL 2017 - RELOADED</span><span class="artist">MARLO KEATS</span><span class="ic h"><svg width="13" height="13" fill="var(--red)"><use href="#i-heart"/></svg></span><span class="ic d"><svg width="13" height="13" stroke="var(--blue)"><use href="#i-down"/></svg></span><span class="ic s"><svg width="13" height="13" stroke="var(--orange)" fill="var(--orange)"><use href="#i-share"/></svg></span></div>
      <div class="row"><span class="thumb" role="img" aria-label="Track cover"></span><span class="play"></span><span class="title">ROCK &amp; ROLL 2017 - RELOADED</span><span class="artist">MARLO KEATS</span><span class="ic h"><svg width="13" height="13" fill="var(--red)"><use href="#i-heart"/></svg></span><span class="ic d"><svg width="13" height="13" stroke="var(--blue)"><use href="#i-down"/></svg></span><span class="ic s"><svg width="13" height="13" stroke="var(--orange)" fill="var(--orange)"><use href="#i-share"/></svg></span></div>
      <div class="row"><span class="thumb" role="img" aria-label="Track cover"></span><span class="play"></span><span class="title">ROCK &amp; ROLL 2017 - RELOADED</span><span class="artist">MARLO KEATS</span><span class="ic h"><svg width="13" height="13" fill="var(--red)"><use href="#i-heart"/></svg></span><span class="ic d"><svg width="13" height="13" stroke="var(--blue)"><use href="#i-down"/></svg></span><span class="ic s"><svg width="13" height="13" stroke="var(--orange)" fill="var(--orange)"><use href="#i-share"/></svg></span></div>
      <div class="row"><span class="thumb" role="img" aria-label="Track cover"></span><span class="play"></span><span class="title">ROCK &amp; ROLL 2017 - RELOADED</span><span class="artist">MARLO KEATS</span><span class="ic h"><svg width="13" height="13" fill="var(--red)"><use href="#i-heart"/></svg></span><span class="ic d"><svg width="13" height="13" stroke="var(--blue)"><use href="#i-down"/></svg></span><span class="ic s"><svg width="13" height="13" stroke="var(--orange)" fill="var(--orange)"><use href="#i-share"/></svg></span></div>
      <div class="row"><span class="thumb" role="img" aria-label="Track cover"></span><span class="play"></span><span class="title">ROCK &amp; ROLL 2017 - RELOADED</span><span class="artist">MARLO KEATS</span><span class="ic h"><svg width="13" height="13" fill="var(--red)"><use href="#i-heart"/></svg></span><span class="ic d"><svg width="13" height="13" stroke="var(--blue)"><use href="#i-down"/></svg></span><span class="ic s"><svg width="13" height="13" stroke="var(--orange)" fill="var(--orange)"><use href="#i-share"/></svg></span></div>
      <div class="row"><span class="thumb" role="img" aria-label="Track cover"></span><span class="play"></span><span class="title">ROCK &amp; ROLL 2017 - RELOADED</span><span class="artist">MARLO KEATS</span><span class="ic h"><svg width="13" height="13" fill="var(--red)"><use href="#i-heart"/></svg></span><span class="ic d"><svg width="13" height="13" stroke="var(--blue)"><use href="#i-down"/></svg></span><span class="ic s"><svg width="13" height="13" stroke="var(--orange)" fill="var(--orange)"><use href="#i-share"/></svg></span></div>
      <div class="row"><span class="thumb" role="img" aria-label="Track cover"></span><span class="play"></span><span class="title">ROCK &amp; ROLL 2017 - RELOADED</span><span class="artist">MARLO KEATS</span><span class="ic h"><svg width="13" height="13" fill="var(--red)"><use href="#i-heart"/></svg></span><span class="ic d"><svg width="13" height="13" stroke="var(--blue)"><use href="#i-down"/></svg></span><span class="ic s"><svg width="13" height="13" stroke="var(--orange)" fill="var(--orange)"><use href="#i-share"/></svg></span></div>
    </div>

    <div class="abs more">MORE MUSIC »</div>
  </section>

  <svg class="abs band" style="top:922px" width="1142" height="49" viewBox="0 0 1142 49">
    <defs><linearGradient id="g2" x1="0" x2="1"><stop offset="0" stop-color="#f6c22a"/><stop offset=".35" stop-color="#f39a1f"/><stop offset=".7" stop-color="#ee5a25"/><stop offset="1" stop-color="#d8283a"/></linearGradient></defs>
    <polygon points="0,48 137,2 1142,46 1142,49 0,49" fill="url(#g2)"/>
  </svg>

  <footer class="abs footer"></footer>
  <div class="abs f-brand">Vorlen Music</div>
  <div class="abs social" aria-label="Social links"><span style="background:#2f6fb7"></span><span style="background:#27a5dd"></span><span style="background:#d9302c"></span></div>
  <nav class="abs f-links" style="left:429px"><span>HOME</span><span>MUSIC</span><span>ARTISTS</span><span>NEWS</span></nav>
  <nav class="abs f-links" style="left:627px"><span>LOGIN</span><span>MY ACCOUNT</span><span>PRIVACY</span><span>CONTACT</span></nav>
  <div class="abs news-h">NEWSLETTER SIGNUP</div>
  <div class="abs email">Email Address</div>
  <div class="abs submit">SUBMIT</div>
  <div class="abs legal">© VORLEN MUSIC | ALL RIGHTS RESERVED</div>
</div>
</body>
</html>
```